Emerging Ed-Tech Startup seeking Stationery Designs!

We are in need of basic set of stationery designs to be used for our business operations, letters, emails, and in-office materials. We are a technology startup enhancing on campus work experience offerings by establishing a collaborative work environment for the completion of such tasks.

Our colors are Vibrant Tiffany Blue/Black/White.

Website: www.campusnorthward.com (Still under construction aside from the landing pages)

Please make sure the designs use a brighter more vibrant tiffany blue color than seen in the image files uploaded. We are not using those materials.

Our logo has been added as a file as well, please use that for any designs (include that logo). Thank you.

```html
<!DOCTYPE html>
<html lang="en">
<head>
<meta charset="utf-8">
<title>CampusNorthward Envelope</title>
<link rel="stylesheet" href="https://fonts.googleapis.com/css2?family=Arimo:wght@400&display=swap">
<style>
  :root {
    --tiffany: #7ff4da;
    --tiffany-text: #4fdcbd;
    --tiffany-pale: #dcfaf4;
    --sea-green: #93cbbb;
    --charcoal: #4d4d4d;
    --ink: #1a1a1a;
    --grey-text: #6b6b6b;
    --paper: #ffffff;
  }
  * { margin: 0; padding: 0; box-sizing: border-box; }
  html, body { width: 1200px; height: 542px; overflow: hidden; background: var(--paper); }
  .envelope {
    position: relative;
    width: 1200px;
    height: 542px;
    background: var(--paper);
    border: 1px solid var(--ink);
    overflow: hidden;
    font-family: "Arimo", Arial, sans-serif;
  }
  .envelope__art {
    position: absolute;
    inset: 0;
    width: 100%;
    height: 100%;
  }
  .brand {
    position: absolute;
    left: 53px;
    top: 49px;
    display: flex;
    align-items: center;
    gap: 24px;
  }
  .brand__square {
    width: 96px;
    height: 96px;
    background: var(--tiffany);
  }
  .brand__name {
    font-size: 29px;
    font-weight: 400;
    color: var(--ink);
    letter-spacing: 0.4px;
  }
  .contact {
    position: absolute;
    left: 52px;
    top: 369px;
    font-size: 11.5px;
    font-style: normal;
    color: var(--grey-text);
    white-space: nowrap;
  }
  .contact__sep { margin: 0 9px; }
  .contact__web { color: var(--tiffany-text); }
</style>
</head>
<body>
  <div class="envelope">
    <svg class="envelope__art" viewBox="0 0 1200 542" aria-hidden="true">
      <rect class="base-band" x="0" y="500" width="1200" height="42" fill="var(--tiffany-pale)"/>
      <rect class="base-line" x="0" y="494" width="620" height="4" fill="var(--tiffany)"/>
      <rect class="base-bar" x="0" y="512" width="240" height="30" fill="var(--charcoal)"/>
      <circle class="corner-ring corner-ring--outer" cx="1200" cy="542" r="300" fill="var(--charcoal)"/>
      <circle class="corner-ring corner-ring--middle" cx="1200" cy="542" r="215" fill="var(--sea-green)"/>
      <circle class="corner-ring corner-ring--inner" cx="1200" cy="542" r="130" fill="var(--tiffany)"/>
      <circle class="corner-ring corner-ring--core" cx="1200" cy="542" r="55" fill="var(--paper)"/>
      <circle class="corner-dot" cx="862" cy="300" r="9" fill="var(--tiffany)"/>
      <circle class="corner-dot" cx="836" cy="330" r="5" fill="var(--sea-green)"/>
    </svg>

    <header class="brand">
      <span class="brand__square"></span>
      <span class="brand__name">CampusNorthward</span>
    </header>

    <address class="contact">
      <span>House # B-14</span><span class="contact__sep">|</span>
      <span>Harbor Avenue</span><span class="contact__sep">|</span>
      <span>+91 23 4477281</span><span class="contact__sep">|</span>
      <span>info@campusnorthward.com</span><span class="contact__sep">|</span>
      <span class="contact__web">www.campusnorthward.com</span>
    </address>
  </div>
</body>
</html>
```